Home Care company needs letter head branding

Home care company needs a letter head which can be used for all documents the company's clients view. We provided in home care for the elderly. We would like to use our company colors (2785A7, 0A4057 and 34A74D) and should not be too large as we will be using it on more than just a letter head but all documents our clients sign / receive.
Target Market(s)
Professional business
Industry/Entity Type
Health Care
Requirements
Must have
- corporate brand colors

```html
<!DOCTYPE html>
<html lang="en">
<head>
<meta charset="utf-8">
<title>Elmhaven Care Letterhead</title>
<link href="https://fonts.googleapis.com/css2?family=Lato:wght@400;700&family=Tinos:wght@400;700&display=swap" rel="stylesheet">
<style>
  :root {
    --brand-blue: #2785A7;
    --brand-navy: #0A4057;
    --brand-green: #A9CC3A;
    --paper: #FBFBFB;
    --ink: #333333;
    --backdrop: #6E6E6E;
    --watermark: #E9EEF1;
  }
  html, body {
    margin: 0;
    width: 1200px;
    height: 1200px;
    overflow: hidden;
    background: var(--backdrop);
  }
  .letterhead {
    position: absolute;
    left: 226px;
    top: 40px;
    width: 653px;
    height: 978px;
    background: var(--paper);
    overflow: hidden;
    transform: scale(1.145);
    transform-origin: top left;
    font-family: "Tinos", "Times New Roman", serif;
    color: var(--ink);
    font-size: 13px;
    line-height: 16px;
  }
  .side-band {
    position: absolute;
    left: 0; top: 0;
    width: 45px; height: 100%;
    background: linear-gradient(180deg, #B3D245, var(--brand-green));
  }
  .watermark-disc {
    position: absolute;
    left: 410px; top: 430px;
    width: 460px; height: 460px;
  }
  .corner-block {
    position: absolute;
    right: 0; bottom: 0;
    width: 42px; height: 152px;
    background: var(--brand-blue);
  }
  .brand {
    position: absolute;
    left: 126px; top: 95px;
    display: flex;
    align-items: center;
    gap: 12px;
  }
  .brand-mark {
    width: 86px; height: 86px;
    border-radius: 50%;
    background: var(--brand-blue);
  }
  .brand-name {
    font-family: "Lato", sans-serif;
    font-weight: 700;
    font-size: 44px;
    line-height: 1;
    color: var(--brand-blue);
  }
  .block { position: absolute; left: 72px; width: 535px; margin: 0; }
  .issue-date { top: 290px; }
  .recipient { top: 354px; }
  .subject { top: 449px; font-weight: 700; }
  .salutation { top: 512px; }
  .para-1 { top: 544px; text-align: justify; }
  .para-2 { top: 607px; text-align: justify; }
  .para-3 { top: 670px; }
  .closing { top: 734px; }
  .contact-list {
    position: absolute;
    left: 72px; top: 899px;
    margin: 0; padding: 0;
    list-style: none;
    font-family: "Lato", sans-serif;
    font-size: 13px;
    line-height: 16.5px;
    color: #222;
  }
  .contact-list li { display: flex; align-items: center; gap: 6px; }
  .contact-list svg { width: 11px; height: 11px; fill: var(--brand-blue); }
  .postal-address {
    position: absolute;
    right: 53px; top: 917px;
    margin: 0;
    text-align: right;
    font-family: "Lato", sans-serif;
    font-style: normal;
    font-size: 13px;
    line-height: 16.5px;
    color: #222;
  }
</style>
</head>
<body>
<main class="letterhead">
  <div class="side-band" role="img" aria-label="Green side band with light leaf pattern"></div>
  <svg class="watermark-disc" viewBox="0 0 460 460" role="img" aria-label="Faint large circular brand decoration">
    <circle cx="230" cy="230" r="220" fill="var(--watermark)" opacity="0.7"/>
  </svg>
  <div class="corner-block" role="img" aria-label="Blue corner band with light leaf pattern"></div>

  <header class="brand">
    <span class="brand-mark"></span>
    <span class="brand-name">Elmhaven Care</span>
  </header>

  <p class="block issue-date">Issuing date: May 5, 2012</p>
  <p class="block recipient">Name of employee: Mr. xyz<br>Address of employee<br>address line 2</p>
  <p class="block subject">Ref: Promotion as an Assistant secretary</p>
  <p class="block salutation">Dear Mr. xyz,</p>
  <p class="block para-1">I have the pleasure to inform you that you have been promoted as assistant secretary in the share department of the company. You are required to take charge of the new assignment on 15<sup style="font-size:8px;line-height:0">th</sup> May, 2012. Please accept my hearty congratulations on your promotion.</p>
  <p class="block para-2">Your salary scale in the promoted cadre will be Tk. 16,000 and from 15th may, your basic salary will be fixed at Tk. 12,000 in the said scale. You will be entitled to all other allowances as applicable to the staff-II of the company. Other services conditions remain unchanged.</p>
  <p class="block para-3">Please acknowledge receipt of this letter.</p>
  <p class="block closing">Yours sincerely,</p>

  <ul class="contact-list">
    <li><svg viewBox="0 0 12 12"><path d="M1 5c0-2 2-3 5-3s5 1 5 3l-2 .5-.5-1.5h-5L3 5.5zM3 6h6l1 4H2z"/></svg>(044) 123456789</li>
    <li><svg viewBox="0 0 12 12"><path d="M1 3h10v6H1z M1 3l5 3.5L11 3" stroke="#fff" stroke-width="0.8"/></svg>info@youremail.com</li>
    <li><svg viewBox="0 0 12 12"><circle cx="6" cy="6" r="5"/></svg>www.yourwebsite.com</li>
  </ul>
  <address class="postal-address">1234, Address GoesHere<br>Country name, 12345</address>
</main>
</body>
</html>
```